Meridane Haulage - Website

A clean, not cluttered informative website for our business. We specialize in the transportation of radioactive materials across North America. The site is mostly for information about our company and will not be used to attract business but will be used to attract employee's mainly drivers. Driver's are very hard to find in our area. One of the pages needs to be a job's posting page with an apply now button. Either an application can be filled out there or a resume can be uploaded which ever functionality works better. I would like a website that I can easily edit, ability to change text and photos.

Number of Pages Required

5+ page

Colors

Designer to choose colors to be used in the design.

Requirements
Must have
• Home - About - Services - Jobs - Contact pages
• A way prospective employee's can apply or upload their resume to be emailed to me
• Very clean apperance
Should not have
• I don't want it to be busy

```html
<!DOCTYPE html>
<html lang="en">
<head>
<meta charset="utf-8">
<title>Meridane Haulage</title>
<link href="https://fonts.googleapis.com/css2?family=Montserrat:wght@400;500;600;700;800&display=swap" rel="stylesheet">
<style>
:root{
  --red:#e3202a;
  --ink:#1d1d1d;
  --muted:#8d8d8d;
  --light:#f2f2f2;
  --dark:#262626;
  --white:#ffffff;
}
*{box-sizing:border-box;margin:0;padding:0}
html,body{width:1200px;height:4787px;overflow:hidden;background:var(--white)}
body{position:relative;font-family:'Montserrat',sans-serif;color:var(--ink)}
.abs{position:absolute}
.brand{font-family:'Montserrat',sans-serif;font-weight:800;letter-spacing:3px;text-transform:uppercase}
.btn{position:absolute;display:flex;align-items:center;justify-content:center;background:var(--red);color:var(--white);font-weight:700;font-size:17px;border-radius:24px;width:240px;height:46px}
.section-title{position:absolute;display:flex;align-items:center;gap:14px;font-weight:800;font-size:24px;letter-spacing:1px;text-transform:uppercase}
.section-title .dot{width:26px;height:26px;border-radius:50%;border:3px solid currentColor;opacity:.7}
.section-title .soft{color:var(--muted)}
p{font-size:16px;line-height:1.6}

/* hero */
.hero{left:0;top:0;width:1200px;height:680px;background:linear-gradient(180deg,#3a3a3a 0%,#6d6d6d 45%,#9a9a9a 75%,#4a4a4a 100%)}
.topbar{left:0;top:0;width:1200px;height:120px;background:linear-gradient(90deg,#111 0%,#2b2b2b 60%,rgba(40,40,40,.4) 100%)}
.logo{left:45px;top:38px;color:var(--white);font-size:26px}
.nav{right:40px;top:46px;display:flex;gap:34px;font-size:15px;font-weight:600;color:#d8d8d8;text-transform:uppercase;letter-spacing:1px}
.nav .active{color:var(--white);border-bottom:2px solid var(--white);padding-bottom:4px}
.hero-curve{left:0;top:520px}
.headline{left:60px;top:700px;width:1080px;text-align:center;font-weight:800;font-size:27px;line-height:1.35;text-transform:uppercase}
.headline .soft{color:var(--muted)}
.map{left:90px;top:805px;width:440px;height:350px;background:linear-gradient(180deg,#3d9ad9 0%,#3d9ad9 55%,#d81e2a 56%,#d81e2a 100%);border-radius:30px 60px 90px 40px}
.intro{left:600px;top:820px;width:510px}
.intro p+p{margin-top:22px}

/* about */
.about{left:0;top:1325px;width:1200px;height:480px;background:var(--light)}
.about .section-title{left:0;width:1200px;top:110px;justify-content:center}
.about p{position:absolute;left:110px;top:180px;width:980px;text-align:center}
.about .btn{left:480px;top:340px}

/* services */
.services{left:0;top:1805px;width:1200px;height:625px;background:linear-gradient(180deg,#1e1e1e,#3a3a3a 60%,#2a2a2a);clip-path:polygon(0 0,100% 0,100% 88%,50% 100%,0 88%)}
.services .section-title{left:0;width:1200px;top:105px;justify-content:center;color:var(--white)}
.services .lead{position:absolute;left:110px;top:165px;width:980px;text-align:center;color:var(--white)}
.svc-label{position:absolute;color:var(--white);font-weight:700;font-size:17px;line-height:1.3}
.svc-icon{position:absolute;width:64px;height:64px;border-radius:50%;background:var(--white);display:flex;align-items:center;justify-content:center}
.center-brand{left:0;width:1200px;top:430px;text-align:center;color:var(--white);font-size:34px}

/* join */
.join .section-title{left:95px;top:2530px}
.join p{position:absolute;left:95px;top:2600px;width:450px}
.join .btn{left:95px;top:2850px}
.join-photo{left:600px;top:2520px;width:510px;height:375px;background:linear-gradient(160deg,#cfe0ef 0%,#e9eef2 45%,#8d9aa5 100%)}

/* news */
.news{left:0;top:3000px;width:1200px;height:660px;background:var(--light)}
.news .section-title{left:0;width:1200px;top:95px;justify-content:center}
.card{position:absolute;top:170px;width:315px;height:410px;background:var(--white);box-shadow:0 2px 10px rgba(0,0,0,.08);padding:20px}
.card .pic{width:275px;height:165px}
.card .date{display:flex;align-items:center;gap:10px;margin-top:20px;font-size:14px}
.card .date i{width:18px;height:18px;border:2px solid var(--red);border-radius:3px;display:block}
.card h3{font-size:15px;font-weight:700;margin-top:16px;line-height:1.4}
.card p{font-size:15px;line-height:1.45}
.card .more{margin-top:16px;color:var(--red);font-size:14px}

/* contact */
.contact{left:0;top:3670px;width:1200px;height:610px;background:linear-gradient(180deg,#2a2a2a,#3b3f33 55%,#232323);clip-path:polygon(0 0,100% 0,100% 86%,50% 100%,0 86%)}
.contact .section-title{left:0;width:1200px;top:105px;justify-content:center;color:var(--white)}
.contact .sub{position:absolute;left:0;width:1200px;top:170px;text-align:center;color:var(--white);font-weight:700;font-size:14px;letter-spacing:1px;text-transform:uppercase}
.field{position:absolute;background:rgba(120,120,120,.55);color:var(--white);font-size:14px;font-weight:600;padding:14px 12px}
.contact .btn{left:480px;top:440px}

/* footer */
.footer-brand{left:0;width:1200px;top:4375px;text-align:center;color:var(--dark);font-size:34px}
.fcol{position:absolute;top:4485px;font-size:13px;line-height:1.55;color:#333}
.fcol h4{font-size:14px;font-weight:800;text-transform:uppercase;padding-bottom:10px;border-bottom:1px solid #ddd;margin-bottom:12px;width:140px}
.row{display:flex;align-items:center;gap:10px;margin-bottom:12px}
.row .ic{width:24px;height:24px;border-radius:50%;border:2px solid #333;flex:none}
.row .sq{width:26px;height:26px;border-radius:50%;background:#333;flex:none}
.nl-input{width:260px;height:34px;background:#eee;font-size:13px;padding:8px 10px;margin:8px 0}
.nl-btn{width:130px;height:32px;background:var(--red);color:var(--white);border-radius:16px;font-weight:700;font-size:13px;display:flex;align-items:center;justify-content:center}
.copyright{left:0;top:4738px;width:1200px;height:49px;background:#000;color:var(--white);font-size:13px;font-weight:700;display:flex;align-items:center;justify-content:center;letter-spacing:.5px}
</style>
</head>
<body>

<div class="abs hero" role="img" aria-label="Photograph of a semi truck hauling radioactive material containers in front of cooling towers"></div>
<div class="abs topbar"></div>
<div class="abs logo brand">Meridane Haulage</div>
<nav class="abs nav">
  <span class="active">Home</span><span>About</span><span>Services</span><span>Jobs</span><span>News</span><span>Contact</span>
</nav>
<svg class="abs hero-curve" width="1200" height="165" viewBox="0 0 1200 165" aria-hidden="true">
  <path d="M0 60 C300 150 800 165 1200 120 L1200 165 L0 165 Z" fill="#ffffff"/>
</svg>

<h1 class="abs headline">Meridane Haulage has been the leader in the <span class="soft">transportation of radioactive materials</span> across North America since 1980</h1>

<div class="abs map" role="img" aria-label="Map of North America with Canada in blue and the United States in red"></div>
<div class="abs intro">
  <p>Lorem ipsum dolor sit amet, consectetur adipiscing elit, sed do eiusmod tempor incididunt ut labore et dolore magna aliqua. Ut enim ad minim veniam, quis nostrud exercitation ullamco laboris nisi ut aliquip ex ea commodo consequat.</p>
  <p>Duis aute irure dolor in reprehenderit in voluptate velit esse cillum dolore eu fugiat nulla pariatur. Excepteur sint occaecat cupidatat non proident, sunt in culpa qui officia des erunt mollit anim id est laborum.</p>
</div>

<section class="abs about">
  <h2 class="section-title"><span class="dot"></span>About <span class="soft">Meridane Haulage</span></h2>
  <p>Lorem ipsum dolor sit amet, consectetur adipiscing elit, sed do eiusmod tempor incididunt ut labore et dolore magna aliqua. Ut enim ad minim veniam, quis nostrud exercitation ullamco laboris nisi ut aliquip ex ea commodo consequat. Duis aute irure dolor in reprehenderit in voluptate velit esse cillum dolore eu fugiat nulla pariatur. Excepteur sint occaecat cupidatat non proident, sunt in culpa qui officia des erunt mollit anim id est laborum.</p>
  <a class="btn">Learn More</a>
</section>

<section class="abs services">
  <h2 class="section-title"><span class="dot"></span>Our Services</h2>
  <p class="lead">We are here to manage your logistical needs from start to finish, and our extensive experience allows us to offer innovative, reliable, and safe front-end nuclear transportation solutions for the following materials:</p>
  <svg class="abs" style="left:0;top:0" width="1200" height="625" aria-hidden="true">
    <g stroke="#ffffff" stroke-width="2" fill="none">
      <circle cx="600" cy="560" r="270"/>
      <line x1="40" y1="312" x2="1160" y2="312"/>
      <line x1="270" y1="432" x2="330" y2="432"/>
      <line x1="870" y1="432" x2="930" y2="432"/>
    </g>
    <g fill="#ffffff">
      <circle cx="430" cy="312" r="7"/><circle cx="770" cy="312" r="7"/>
      <circle cx="330" cy="432" r="7"/><circle cx="870" cy="432" r="7"/>
    </g>
  </svg>
  <div class="svc-label" style="left:62px;top:302px">Uranium ore concentrates</div>
  <div class="svc-icon" style="left:330px;top:280px"><svg width="30" height="30" viewBox="0 0 30 30"><circle cx="15" cy="15" r="4" fill="#222"/><circle cx="15" cy="15" r="12" fill="none" stroke="#222" stroke-width="2"/></svg></div>
  <div class="svc-icon" style="left:806px;top:280px"><svg width="30" height="30" viewBox="0 0 30 30"><path d="M8 26 L12 6 L18 6 L22 26 Z" fill="#222"/></svg></div>
  <div class="svc-label" style="left:890px;top:302px">Uranium trioxide</div>
  <div class="svc-label" style="left:62px;top:410px">Natural and<br>enriched uranium<br>hexafluoride</div>
  <div class="svc-icon" style="left:236px;top:400px"><svg width="30" height="30" viewBox="0 0 30 30"><rect x="8" y="5" width="14" height="20" rx="2" fill="#222"/></svg></div>
  <div class="svc-icon" style="left:900px;top:400px"><svg width="30" height="30" viewBox="0 0 30 30"><path d="M15 4 C10 12 8 16 8 19 a7 7 0 0 0 14 0 C22 16 20 12 15 4Z" fill="#222"/></svg></div>
  <div class="svc-label" style="left:985px;top:410px">Fuel pellets<br>and bundles</div>
  <div class="abs brand center-brand">Meridane Haulage</div>
</section>

<section class="join">
  <h2 class="section-title"><span class="dot"></span>Join <span class="soft">Meridane</span> Team</h2>
  <p>Lorem ipsum dolor sit amet, consectetur adipiscing elit, sed do eiusmod tempor incididunt ut labore et dolore magna aliqua. Ut enim ad minim veniam, quis nostrud exercitation ullamco laboris nisi ut aliquip ex ea commodo consequat. Duis aute irure dolor in reprehenderit in voluptate velit esse cillum dolore eu fugiat nulla pariatur excepteur sint occaecat cupi.</p>
  <a class="btn">Apply Now</a>
  <div class="abs join-photo" role="img" aria-label="Photograph of a driver holding a tablet in front of a row of white trucks"></div>
</section>

<section class="abs news">
  <h2 class="section-title"><span class="dot"></span>Latest <span class="soft">News</span></h2>
  <article class="card" style="left:85px">
    <div class="pic" role="img" aria-label="Photograph of an industrial plant at sunset" style="background:linear-gradient(180deg,#5a4a3a,#d07a2a 60%,#2a2018)"></div>
    <div class="date"><i></i>Jan 19, 2019</div>
    <h3>Duis aute irure dolor in reprehen</h3>
    <p>Lorem ipsum dolor sit amet, cons ectetur adipiscing elit, sed do eius mod tempor incididunt.</p>
    <div class="more">Read more...</div>
  </article>
  <article class="card" style="left:442px">
    <div class="pic" role="img" aria-label="Photograph of a city skyline at dusk" style="background:linear-gradient(180deg,#3a6fb0,#1d3a66 60%,#e0a050)"></div>
    <div class="date"><i></i>Jan 17, 2019</div>
    <h3>Duis aute irure dolor in reprehen</h3>
    <p>Lorem ipsum dolor sit amet, cons ectetur adipiscing elit, sed do eius mod tempor incididunt.</p>
    <div class="more">Read more...</div>
  </article>
  <article class="card" style="left:798px">
    <div class="pic" role="img" aria-label="Photograph of a power plant with chimneys" style="background:linear-gradient(180deg,#7fb2e0,#c9d9e6 55%,#7a6a55)"></div>
    <div class="date"><i></i>Jan 14, 2019</div>
    <h3>Duis aute irure dolor in reprehen</h3>
    <p>Lorem ipsum dolor sit amet, cons ectetur adipiscing elit, sed do eius mod tempor incididunt.</p>
    <div class="more">Read more...</div>
  </article>
</section>

<section class="abs contact" role="img" aria-label="Background photograph of radioactive material barrels">
  <h2 class="section-title"><span class="dot"></span>Contact Us</h2>
  <div class="sub">Let us know what you need</div>
  <div class="field" style="left:120px;top:225px;width:300px;height:45px">Your Name</div>
  <div class="field" style="left:452px;top:225px;width:300px;height:45px">Your Email</div>
  <div class="field" style="left:784px;top:225px;width:300px;height:45px">Your Subject</div>
  <div class="field" style="left:120px;top:290px;width:964px;height:130px">Message</div>
  <a class="btn">Send Message</a>
</section>

<div class="abs brand footer-brand">Meridane Haulage</div>

<div class="fcol" style="left:75px">
  <h4>Quick Links</h4>
  Home<br>About<br>Services<br>Jobs<br>Contact
</div>
<div class="fcol" style="left:240px">
  <h4>Transport Services</h4>
  Uranium ore concentrates<br>Uranium hexafluoride<br>Uranium trioxide<br>Fuel pellets and bundles
</div>
<div class="fcol" style="left:470px">
  <h4>Contact</h4>
  <div class="row"><span class="ic"></span><span>Meridane Haulage<br>48 Harlow Ridge Rd<br>Dunmore, PA 18512</span></div>
  <div class="row"><span class="ic"></span><span>1800.555.0142</span></div>
  <div class="row"><span class="ic"></span><span>info@meridanehaulage.com</span></div>
</div>
<div class="fcol" style="left:705px">
  <h4>Follow Us</h4>
  <div class="row"><span class="sq"></span><span>Community</span></div>
  <div class="row"><span class="sq"></span><span>Updates</span></div>
  <div class="row"><span class="sq"></span><span>Photos</span></div>
</div>
<div class="fcol" style="left:870px">
  <h4>Newsletter</h4>
  <strong>Register your email address to<br>get more information about us</strong>
  <div class="nl-input">Email Address</div>
  <div class="nl-btn">SUBSCRIBE</div>
</div>

<div class="abs copyright">COPYRIGHT © 2019 MERIDANE HAULAGE. ALL RIGHTS RESERVED.</div>

</body>
</html>
```